22nd Annual Westbrook Open Cinema Showcase POSTER

Need a modern stylish chic poster for WBOCS's 22nd film festival. Must appeal to our upscale audience and interest new attendees.
Dates are August 23 - 30th, 2019 www.wbocs-example.org

Target Market(s)

we demo flyer attached

Industry/Entity Type

Film Production

Colors

Designer to choose colors to be used in the design.

Requirements
Must have
• Modern, chic, stylish - EYE catching
Nice to have
• Obscure - different - something new
Should not have
• NO CLIP ART

```html
<!DOCTYPE html>
<html lang="en">
<head>
<meta charset="utf-8">
<title>WBOCS 22 Festival Poster</title>
<link href="https://fonts.googleapis.com/css2?family=Montserrat:wght@400;500;600;800&family=Josefin+Sans:wght@400;600;700&family=Oswald:wght@500&display=swap" rel="stylesheet">
<style>
  :root {
    --page: #ececec;
    --teal-core: #1d7895;
    --teal-mid: #10475c;
    --teal-edge: #0a2533;
    --white: #ffffff;
    --green: #8cc63f;
    --rule: rgba(255,255,255,0.55);
    --reel-light: #8a8580;
    --reel-dark: #2a2a2a;
  }
  html, body { margin: 0; padding: 0; width: 1200px; height: 1200px; overflow: hidden; background: var(--page); }
  .poster {
    position: absolute; left: 262px; top: 99px; width: 676px; height: 1002px;
    background: radial-gradient(ellipse 70% 55% at 50% 38%, var(--teal-core) 0%, var(--teal-mid) 55%, var(--teal-edge) 100%);
    color: var(--white); overflow: hidden;
  }
  .brand { position: absolute; left: 0; right: 0; top: 45px; text-align: center; }
  .brand-dot { width: 46px; height: 46px; border-radius: 50%; background: var(--green); margin: 0 auto 10px; }
  .brand-name { font-family: "Montserrat", sans-serif; font-weight: 600; font-size: 46px; letter-spacing: 4px; line-height: 1; }
  .brand-rule { width: 198px; height: 1px; background: var(--rule); margin: 8px auto 6px; }
  .brand-tagline { font-family: "Oswald", sans-serif; font-weight: 500; font-size: 11px; letter-spacing: 0.6px; }
  .hero-art { position: absolute; left: 186px; top: 240px; width: 340px; height: 280px; }
  .edition {
    position: absolute; left: 50px; top: 548px;
    font-family: "Montserrat", sans-serif; font-weight: 800; font-size: 215px; line-height: 1;
    letter-spacing: 0; transform: scaleX(0.84); transform-origin: left top;
  }
  .festival { position: absolute; left: 289px; top: 565px; font-family: "Montserrat", sans-serif; font-weight: 400; font-size: 72px; line-height: 1; }
  .dates { position: absolute; left: 290px; top: 634px; color: var(--green); font-family: "Montserrat", sans-serif; font-weight: 400; font-size: 42px; line-height: 41px; letter-spacing: -1px; }
  .dates sup { font-size: 27px; vertical-align: 14px; line-height: 0; }
  .year { position: absolute; left: 450px; top: 637px; color: var(--green); font-family: "Montserrat", sans-serif; font-weight: 400; font-size: 90px; line-height: 1; letter-spacing: -4px; }
  .location { position: absolute; left: 56px; top: 738px; font-family: "Josefin Sans", sans-serif; font-weight: 400; font-size: 22px; letter-spacing: 8.2px; white-space: nowrap; }
  .location strong { font-weight: 700; }
  .divider { position: absolute; left: 58px; top: 786px; width: 570px; height: 1px; background: var(--rule); }
  .honorees { position: absolute; left: 52px; width: 580px; top: 794px; margin: 0; text-align: center; font-family: "Josefin Sans", sans-serif; font-size: 17px; line-height: 28px; }
  .honorees .name { font-weight: 700; font-variant: small-caps; }
  .site { position: absolute; left: 0; right: 0; top: 937px; text-align: center; color: var(--green); font-family: "Josefin Sans", sans-serif; font-weight: 600; font-size: 22px; letter-spacing: 6px; }
</style>
</head>
<body>
  <main class="poster">
    <header class="brand">
      <div class="brand-dot"></div>
      <div class="brand-name">WBOCS</div>
      <div class="brand-rule"></div>
      <div class="brand-tagline">WESTBROOK OPEN CINEMA SHOWCASE</div>
    </header>

    <svg class="hero-art" viewBox="0 0 340 280" role="img" aria-label="Photograph of a metal film reel fused with a light bulb screw base, resting on its side">
      <defs>
        <radialGradient id="reelTone" cx="45%" cy="45%" r="60%">
          <stop offset="0%" stop-color="var(--reel-light)"/>
          <stop offset="100%" stop-color="var(--reel-dark)"/>
        </radialGradient>
        <radialGradient id="floorShadow" cx="50%" cy="50%" r="50%">
          <stop offset="0%" stop-color="rgba(0,0,0,0.45)"/>
          <stop offset="100%" stop-color="rgba(0,0,0,0)"/>
        </radialGradient>
      </defs>
      <ellipse cx="170" cy="268" rx="160" ry="10" fill="url(#floorShadow)"/>
      <circle cx="136" cy="136" r="130" fill="url(#reelTone)"/>
    </svg>

    <div class="edition">22</div>
    <div class="festival">FESTIVAL</div>
    <div class="dates">August<br>23-30<sup>th</sup></div>
    <div class="year">2019</div>

    <div class="location">Larkmoor | Bayhaven <strong>California</strong></div>
    <div class="divider"></div>

    <p class="honorees">WBOCS’s past honorees include: <span class="name">Marcus Lindell, Paula Marsden, Roland Dressner, Clara Lindqvist, Rosa Merano, Theo Carden, Rosalind Barrow, Hazel Hartley, Zane Quillan, Silas Zorn</span> and <span class="name">Tobin Lattimer.</span></p>

    <div class="site">www.wbocs-example.org</div>
  </main>
</body>
</html>
```